Business Card (I don't have a logo)

I'm bootstrapping a new venture and need a business card and "look" for it. I'd like to print one side only, but could do a bleed to the edges, but don't need to. See my website: www.calebharrowpartners.example to get a sense of the photos that relate to the look/feel of my company.

Target Market(s)

high tech start-up company CEO's in Silicon Valley

Industry/Entity Type

Business

Requirements
Must have
• a look that can cut/paste onto my website that integrates easily with the front page photo. see www.calebharrowpartners.example

```html
<!DOCTYPE html>
<html lang="en">
<head>
<meta charset="utf-8">
<title>Caleb Harrow Partners — Business Card</title>
<link rel="stylesheet" href="https://fonts.googleapis.com/css2?family=Fira+Sans:wght@800&family=Questrial&display=swap">
<style>
  :root {
    --page: #ffffff;
    --card-blue: #006cbd;
    --ink-white: #ffffff;
    --label-grey: #a9a9ae;
    --art-light: rgba(255, 255, 255, 0.92);
    --art-mid: rgba(190, 220, 242, 0.55);
    --art-fade: rgba(120, 180, 225, 0);
  }
  html, body {
    margin: 0;
    padding: 0;
    width: 1200px;
    height: 879px;
    overflow: hidden;
    background: var(--page);
  }
  .canvas {
    position: relative;
    width: 1200px;
    height: 879px;
  }
  .card {
    position: absolute;
    left: 151px;
    top: 145px;
    width: 922px;
    height: 540px;
    background: var(--card-blue);
    overflow: hidden;
  }
  .brand-name {
    position: absolute;
    left: 40px;
    top: 36px;
    width: 424px;
    margin: 0;
    text-align: right;
    font-family: "Fira Sans", "Helvetica Neue", Arial, sans-serif;
    font-weight: 800;
    font-size: 62px;
    line-height: 58px;
    letter-spacing: 0;
    color: var(--ink-white);
  }
  .brand-name span { display: block; }
  .mountain-art {
    position: absolute;
    left: 436px;
    top: 45px;
    width: 476px;
    height: 240px;
    background:
      radial-gradient(ellipse 70% 90% at 75% 35%, var(--art-light) 0%, var(--art-mid) 55%, var(--art-fade) 100%);
  }
  .contact-list {
    position: absolute;
    left: 46px;
    top: 290px;
    margin: 0;
    padding: 0;
    list-style: none;
    font-family: "Questrial", "Century Gothic", sans-serif;
    font-size: 35px;
    line-height: 53.5px;
    color: var(--ink-white);
  }
  .contact-list li { white-space: nowrap; }
  .contact-label {
    display: inline-block;
    width: 46px;
    color: var(--label-grey);
    font-size: 30px;
  }
  .contact-value { letter-spacing: 4px; }
  .contact-value.phone { letter-spacing: 10px; word-spacing: 10px; }
  .contact-value.email { letter-spacing: 2.6px; }
</style>
</head>
<body>
<div class="canvas">
  <section class="card">
    <h1 class="brand-name">
      <span>caleb harrow</span>
      <span>partners</span>
    </h1>
    <div class="mountain-art" role="img" aria-label="Illustration area: snow-capped mountain peak reflected in still water"></div>
    <ul class="contact-list">
      <li><span class="contact-label">p</span><span class="contact-value phone">000 000 0000</span></li>
      <li><span class="contact-label">c</span><span class="contact-value phone">000 000 0000</span></li>
      <li><span class="contact-label">e</span><span class="contact-value email">info@calebharrowpartners.example</span></li>
      <li><span class="contact-label">w</span><span class="contact-value">calebharrowpartners.example</span></li>
    </ul>
  </section>
</div>
</body>
</html>
```